Property letting UK website

I need a web design for a new Property letting company in the UK. I already have a logo that was produced and won by a brief forge logo designer last week.

I like modern designs and require ease of functionality and usage. I already have a domain name registered so need to be able to link to that domain.

Regards,

Morven.

Target Market(s)

UK property

Industry/Entity Type

It Company

Number of Pages Required

5+ page

Requirements
Must have
• Home page, Current properties to let page, About us page, Contact us page, Testimonials page and ability to link to twitter and Facebook account.

```html
<!DOCTYPE html>
<html lang="en">
<head>
<meta charset="utf-8">
<title>Dwellwise – Property Letting</title>
<link href="https://fonts.googleapis.com/css2?family=Yanone+Kaffeesatz:wght@400;700&display=swap" rel="stylesheet">
<style>
  :root{
    --header-bg:#26272b;
    --header-bg-2:#2c2d31;
    --nav-text:#ffffff;
    --accent:#1fb8dc;
    --band-bg:#e3e7ea;
    --label:#2b2c30;
  }
  *{margin:0;padding:0;box-sizing:border-box}
  html,body{width:1200px;height:1200px;overflow:hidden}
  body{font-family:"Yanone Kaffeesatz",sans-serif;background:var(--band-bg);position:relative}
  .site-header{
    position:absolute;left:0;top:0;width:1200px;height:301px;
    background:linear-gradient(180deg,var(--header-bg-2),var(--header-bg));
  }
  .brand{
    position:absolute;top:72px;left:0;width:1200px;
    display:flex;justify-content:center;align-items:center;gap:18px;
  }
  .brand-dot{width:22px;height:22px;border-radius:50%;background:var(--accent)}
  .brand-name{font-size:88px;font-weight:400;color:var(--nav-text);letter-spacing:2px;line-height:1}
  .main-nav{
    position:absolute;top:228px;left:0;width:1200px;
    display:flex;justify-content:center;gap:54px;
  }
  .main-nav a{
    font-size:25px;font-weight:700;font-style:italic;color:var(--nav-text);
    text-decoration:none;text-transform:uppercase;line-height:38px;
  }
  .main-nav a.is-active{color:var(--accent)}
  .hero{
    position:absolute;left:0;top:301px;width:1200px;height:717px;
    background:linear-gradient(160deg,#8a9aa3 0%,#8b8784 35%,#9d958f 55%,#5b5f48 80%,#46502f 100%);
  }
  .slider-toggle{
    position:absolute;left:562px;top:975px;width:86px;height:86px;border-radius:50%;
    background:var(--accent);display:flex;align-items:center;justify-content:center;
  }
  .services{position:absolute;left:0;top:1018px;width:1200px;height:182px}
  .service{position:absolute;top:104px;width:240px;margin-left:-120px;text-align:center}
  .service svg{display:block;margin:0 auto}
  .service-title{
    margin-top:14px;font-size:32px;font-weight:700;font-style:italic;
    color:var(--label);text-transform:uppercase;letter-spacing:1px;
  }
</style>
</head>
<body>
  <header class="site-header">
    <div class="brand">
      <span class="brand-dot"></span>
      <span class="brand-name">Dwellwise</span>
    </div>
    <nav class="main-nav">
      <a href="#" class="is-active">Home</a>
      <a href="#">About</a>
      <a href="#">How it works</a>
      <a href="#">Services</a>
      <a href="#">Blog</a>
      <a href="#">Contacts</a>
    </nav>
  </header>

  <div class="hero" role="img" aria-label="Photo of a large grey stone family house with arched windows, trees and a driveway"></div>

  <a class="slider-toggle" href="#" aria-label="Next slide">
    <svg width="42" height="32" viewBox="0 0 42 32"><path d="M14 4 3 16l11 12M28 4l11 12-11 12" fill="none" stroke="#fff" stroke-width="3.5" stroke-linecap="round" stroke-linejoin="round"/></svg>
  </a>

  <section class="services">
    <div class="service" style="left:155px">
      <svg width="56" height="40" viewBox="0 0 56 40"><rect x="1" y="2" width="54" height="36" rx="3" fill="var(--accent)"/><rect x="6" y="7" width="44" height="26" rx="2" fill="none" stroke="#fff" stroke-width="2"/><circle cx="28" cy="20" r="9" fill="#fff"/><text x="28" y="25" font-size="14" text-anchor="middle" fill="var(--accent)" font-family="sans-serif" font-weight="700">1</text></svg>
      <div class="service-title">Loans</div>
    </div>
    <div class="service" style="left:455px">
      <svg width="50" height="46" viewBox="0 0 50 46"><path d="M25 2C12 2 2 11 2 22c3-3 7-3 10 0 3-3 7-3 10 0h6c3-3 7-3 10 0 3-3 7-3 10 0C48 11 38 2 25 2z" fill="var(--accent)"/><path d="M25 22v17a4 4 0 0 1-8 0" fill="none" stroke="var(--accent)" stroke-width="3" stroke-linecap="round"/></svg>
      <div class="service-title">Mortgages</div>
    </div>
    <div class="service" style="left:755px">
      <svg width="48" height="40" viewBox="0 0 48 40"><path d="M24 2 2 21h6v17h12V27h8v11h12V21h6z" fill="var(--accent)"/></svg>
      <div class="service-title">Rentals</div>
    </div>
    <div class="service" style="left:1053px">
      <svg width="48" height="46" viewBox="0 0 48 46"><circle cx="14" cy="14" r="11" fill="none" stroke="var(--accent)" stroke-width="6"/><path d="M22 22l22 20M36 35l5-5M30 30l4-4" stroke="var(--accent)" stroke-width="6" stroke-linecap="round"/></svg>
      <div class="service-title">Office spaces</div>
    </div>
  </section>
</body>
</html>
```